Health care technology software systems

We have a solid logo. We have company colors that will need to be used as well. We just need a great business card design. We sell to health plans but want to be modern

Target Market(s)

Health technology sector selling into Health Plans

Industry/Entity Type

Health Care Technology

Contact Information for Business Card

Name, title, address, phone number, email

Requirements
Must have
• Use of Parvexa corporate colors - Uploaded w/ our logos

```html
<!DOCTYPE html>
<html lang="en">
<head>
<meta charset="utf-8">
<title>Parvexa Business Card</title>
<link rel="stylesheet" href="https://fonts.googleapis.com/css2?family=Montserrat:wght@300;400;500;700&display=swap">
<style>
  :root {
    --backdrop: #4a4a4c;
    --card-white: #ffffff;
    --brand-navy: #3a55a0;
    --brand-sky: #29a8e0;
    --brand-green: #8dc63f;
    --ink: #1f1f1f;
    --ink-soft: #3d3d3d;
  }
  * { box-sizing: border-box; margin: 0; padding: 0; }
  html, body {
    width: 1200px; height: 1021px; overflow: hidden;
    background: var(--backdrop);
    font-family: "Montserrat", sans-serif;
  }
  .canvas { position: relative; width: 1200px; height: 1021px; }
  .card {
    position: absolute; left: 233px; width: 739px; height: 427px;
    border-radius: 26px;
    box-shadow: 0 6px 14px rgba(0,0,0,0.45);
    overflow: hidden;
  }
  .card--front { top: 65px; background: var(--card-white); }
  .card--back { top: 511px; background: var(--brand-navy); }

  .brand { position: absolute; display: flex; align-items: center; }
  .brand__dot { border-radius: 50%; flex: none; }
  .brand__name { font-weight: 300; line-height: 1; letter-spacing: 1px; }

  .card--front .brand { left: 114px; top: 57px; height: 95px; }
  .card--front .brand__dot { width: 88px; height: 88px; background: var(--brand-navy); }
  .card--front .brand__name { margin-left: 42px; font-size: 98px; color: var(--ink-soft); }

  .card--back .brand { left: 149px; top: 172px; height: 81px; }
  .card--back .brand__dot { width: 76px; height: 76px; background: var(--card-white); }
  .card--back .brand__name { margin-left: 40px; font-size: 86px; color: var(--card-white); }

  .holder__name {
    position: absolute; left: 0; right: 0; top: 214px; text-align: center;
    font-weight: 700; font-size: 24px; color: var(--brand-sky); letter-spacing: 0.2px;
    padding-left: 6px;
  }
  .holder__rule {
    position: absolute; top: 264px; height: 2px; background: var(--brand-sky);
  }
  .holder__rule--left { left: 27px; width: 270px; }
  .holder__rule--right { left: 447px; width: 266px; }
  .holder__title {
    position: absolute; left: 0; right: 0; top: 249px; text-align: center;
    font-weight: 400; font-size: 23px; color: var(--ink); padding-left: 6px;
  }

  .contact { position: absolute; left: 28px; top: 309px; list-style: none; }
  .contact__item {
    display: flex; align-items: center; height: 29px;
    font-size: 18px; color: var(--ink);
  }
  .contact__icon { width: 21px; height: 21px; margin-right: 10px; flex: none; }

  .address {
    position: absolute; right: 28px; top: 340px; text-align: right;
    font-style: normal; font-size: 18px; line-height: 27px; color: var(--ink);
  }
</style>
</head>
<body>
<main class="canvas">
  <section class="card card--front">
    <div class="brand">
      <span class="brand__dot"></span>
      <span class="brand__name">parvexa</span>
    </div>

    <p class="holder__name">ELVAN TORREY</p>
    <span class="holder__rule holder__rule--left"></span>
    <p class="holder__title">Co-Founder</p>
    <span class="holder__rule holder__rule--right"></span>

    <ul class="contact">
      <li class="contact__item">
        <svg class="contact__icon" viewBox="0 0 24 24" aria-hidden="true">
          <path fill="var(--brand-sky)" d="M6.6 10.8c1.4 2.8 3.8 5.1 6.6 6.6l2.2-2.2c.3-.3.7-.4 1-.2 1.1.4 2.3.6 3.6.6.6 0 1 .4 1 1V20c0 .6-.4 1-1 1C10.6 21 3 13.4 3 4c0-.6.4-1 1-1h3.5c.6 0 1 .4 1 1 0 1.3.2 2.5.6 3.6.1.3 0 .7-.2 1L6.6 10.8z"/>
          <path fill="none" stroke="var(--brand-sky)" stroke-width="1.8" d="M14 3.5a6.5 6.5 0 0 1 6.5 6.5M14 7a3 3 0 0 1 3 3"/>
        </svg>
        555-214-7380
      </li>
      <li class="contact__item">
        <svg class="contact__icon" viewBox="0 0 24 24" aria-hidden="true">
          <rect x="2" y="5" width="20" height="14" fill="var(--brand-sky)"/>
          <path fill="none" stroke="#fff" stroke-width="1.5" d="M2.5 5.5 12 13l9.5-7.5M2.5 18.5l7-6M21.5 18.5l-7-6"/>
        </svg>
        info@parvexa.com
      </li>
      <li class="contact__item">
        <svg class="contact__icon" viewBox="0 0 24 24" aria-hidden="true">
          <circle cx="12" cy="12" r="10" fill="var(--brand-sky)"/>
          <path fill="#fff" d="M7 6c2 0 3 1.5 2.5 3s-2 1-2 2.5S9 14 8 16c-1 1-3-2-3.5-4C4.5 9 5.5 6.5 7 6zM14 4.5c2 .5 3 2 2 3s-2.5 0-2.5 1.5 2 1.5 3 2.5-.5 4-2 5.5c-.8-1.5-1.5-3-3-3.5s-1-3 0-4-1.5-2 .5-5z"/>
        </svg>
        www.parvexa.com
      </li>
    </ul>

    <address class="address">
      1840 N. Harbor Lane<br>
      Suite 402 Dunmore.14
    </address>
  </section>

  <section class="card card--back">
    <div class="brand">
      <span class="brand__dot"></span>
      <span class="brand__name">parvexa</span>
    </div>
  </section>
</main>
</body>
</html>
```